Local Roofing/Construction company business needs new biz card design

We need a new business card design, current cards are from the start of this operation and generic at best. We are a local Construction Company (General Contractor) with a majority of our work originating from insurance claims-exterior finish work is the main focus (Roofs-Siding-Gutters etc). Heavily involved with homeowners and the low ball offers they receive from insurance company's after a insurable event takes place. I have attached some of our original logo file(s) below.

```html
<!DOCTYPE html>
<html lang="en">
<head>
<meta charset="utf-8">
<title>Ridgeline Construction – Business Card</title>
<link href="https://fonts.googleapis.com/css2?family=Montserrat:wght@400;500;600;800&display=swap" rel="stylesheet">
<style>
  :root {
    --backdrop: #3a3b3c;
    --card: #02191f;
    --card-deep: #00131a;
    --accent: #1ee38a;
    --ink: #f4f6f5;
    --muted: #54656a;
    --emboss: #1f3a40;
  }
  * { box-sizing: border-box; margin: 0; padding: 0; }
  html, body {
    width: 1200px; height: 1200px; overflow: hidden;
    background: var(--backdrop);
    font-family: "Montserrat", sans-serif;
  }
  .canvas { position: relative; width: 1200px; height: 1200px; }
  .card {
    position: absolute; left: 150px;
    width: 900px; height: 514px;
    border-radius: 34px;
    background: radial-gradient(ellipse at 60% 20%, #06262d 0%, var(--card) 55%, var(--card-deep) 100%);
    border-bottom: 4px solid var(--accent);
    box-shadow: 0 14px 30px rgba(0,0,0,.45);
    overflow: hidden;
  }
  .card--front { top: 50px; }
  .card--back { top: 630px; }

  .brand {
    position: absolute; top: 92px; left: 0; right: 0;
    display: flex; align-items: center; justify-content: center; gap: 22px;
  }
  .brand__mark { width: 70px; height: 70px; background: var(--accent); }
  .brand__name {
    font-weight: 800; font-size: 46px; letter-spacing: 2px;
    color: var(--ink); line-height: 1; text-transform: uppercase;
  }

  .holder { position: absolute; left: 86px; top: 330px; }
  .holder__name {
    font-weight: 600; font-size: 48px; color: var(--accent);
    letter-spacing: .5px; line-height: 1;
  }
  .holder__role {
    margin-top: 6px; font-weight: 400; font-size: 24px; color: var(--ink);
    letter-spacing: 1px;
  }

  .divider {
    position: absolute; left: 470px; top: 250px;
    width: 1.5px; height: 190px; background: var(--muted);
  }

  .contacts {
    position: absolute; left: 510px; top: 242px;
    list-style: none;
  }
  .contacts li {
    display: flex; align-items: flex-start; gap: 14px;
    font-size: 21px; color: var(--ink); line-height: 1.2;
    margin-bottom: 12px;
  }
  .contacts svg { flex: none; width: 22px; height: 22px; margin-top: 2px; }

  .back-brand {
    position: absolute; left: 50%; top: 50%;
    transform: translate(-50%, -50%);
    display: flex; align-items: center; gap: 24px;
  }
  .back-brand__mark {
    width: 150px; height: 150px; background: var(--emboss);
    border-radius: 14px;
  }
  .back-brand__name {
    font-weight: 800; font-size: 44px; letter-spacing: 2px;
    color: var(--emboss); text-transform: uppercase; line-height: 1.05;
  }
</style>
</head>
<body>
<main class="canvas">
  <section class="card card--front">
    <div class="brand">
      <span class="brand__mark"></span>
      <span class="brand__name">Ridgeline Construction</span>
    </div>

    <div class="holder">
      <p class="holder__name">FULL NAME</p>
      <p class="holder__role">POSITION</p>
    </div>

    <span class="divider"></span>

    <ul class="contacts">
      <li>
        <svg viewBox="0 0 24 24" fill="var(--accent)"><path d="M6.6 10.8a15.1 15.1 0 0 0 6.6 6.6l2.2-2.2a1 1 0 0 1 1-.25 11.4 11.4 0 0 0 3.6.57 1 1 0 0 1 1 1V20a1 1 0 0 1-1 1A17 17 0 0 1 3 4a1 1 0 0 1 1-1h3.5a1 1 0 0 1 1 1c0 1.25.2 2.45.57 3.6a1 1 0 0 1-.25 1z"/></svg>
        555-013-4720
      </li>
      <li>
        <svg viewBox="0 0 24 24" fill="none" stroke="var(--accent)" stroke-width="1.8"><circle cx="12" cy="12" r="9.5"/><ellipse cx="12" cy="12" rx="4.2" ry="9.5"/><path d="M2.5 12h19M4 7h16M4 17h16"/></svg>
        www.ridgelinebuilds.com
      </li>
      <li>
        <svg viewBox="0 0 24 24" fill="var(--accent)"><path d="M2 5h20v14H2z" opacity=".9"/><path d="M2 5l10 8 10-8" fill="none" stroke="var(--card)" stroke-width="1.8"/></svg>
        hello@ridgelinebuilds.com
      </li>
      <li>
        <svg viewBox="0 0 24 24" fill="var(--accent)"><path d="M12 2a7 7 0 0 0-7 7c0 5.2 7 13 7 13s7-7.8 7-13a7 7 0 0 0-7-7zm0 9.5A2.5 2.5 0 1 1 12 6.5a2.5 2.5 0 0 1 0 5z"/></svg>
        <span>42 Harbor Oak Ln<br>Fairview, MO 60000</span>
      </li>
    </ul>
  </section>

  <section class="card card--back">
    <div class="back-brand">
      <span class="back-brand__mark"></span>
      <span class="back-brand__name">Ridgeline<br>Construction</span>
    </div>
  </section>
</main>
</body>
</html>
```